Business Card Design Project

We store & repair empty shipping containers owned by the shipping lines.
We have just selected a logo design & now want a business card & letterhead to go with it. (Logo is attached - colours are yellow & dark grey)

ABN: 384 902 17736 (only need to be small)
ACN: 293 718 406 (only need to be small)

Address: 218-220 Tallowby Rd, Carrow Flats, 3094
Website: www.harbinvault.com.au

You will need to make provision for a phone number, fax number & email (which we don't have yet.. so okay to just put in fake ones)
Updates

Target Market(s)

Professionals - shipping lines, freight forwarders,

Industry/Entity Type

Shipping

Requirements
Must have
• Must include the logo attached.
Must include ABN & ACN, address, phone as per above
Please make allowance for a persons name & their position eg:
Glen Whitcombe, Manager & enough space so we could possibly add their mobile or email address afterwards. Glens phone number is 0498 305217 although we don't have an email address set up yet. A lott depends it the card starts to look too crowded if we'll add it in or not.
Nice to have
• Must be easy to read -prefer to keep it simple

```html
<!DOCTYPE html>
<html lang="en">
<head>
<meta charset="utf-8">
<title>Harbin Vault – Letterhead &amp; Business Card</title>
<link rel="stylesheet" href="https://fonts.googleapis.com/css2?family=Montserrat:wght@400;500;600;700&display=swap">
<style>
  :root {
    --yellow: #f7bb16;
    --charcoal: #3a4750;
    --ink: #4a4f55;
    --ink-strong: #2f3438;
    --rule: #9aa0a5;
    --paper: #ffffff;
    --paper-shade: #f5f6f8;
    --board: #ffffff;
  }
  * { margin: 0; padding: 0; box-sizing: border-box; }
  html, body { width: 1200px; height: 933px; overflow: hidden; background: var(--board); }
  body { position: relative; font-family: "Montserrat", sans-serif; color: var(--ink); }

  .letterhead {
    position: absolute; left: 351px; top: 94px; width: 576px; height: 744px;
    background: linear-gradient(97deg, var(--paper-shade) 0%, var(--paper) 20%, #f7f8f9 35%, var(--paper) 55%, #fafafb 70%, var(--paper) 85%);
    box-shadow: 0 1px 3px rgba(0,0,0,.25);
    overflow: hidden;
  }
  .letterhead .stripes { position: absolute; left: 0; top: 0; }
  .letterhead .brand { position: absolute; left: 412px; top: 70px; }
  .brand-name {
    font-weight: 700; font-size: 19px; letter-spacing: -0.2px;
    color: var(--charcoal); white-space: nowrap; line-height: 1;
  }
  .letterhead-footer {
    position: absolute; left: 23px; top: 686px;
    font-size: 8.6px; line-height: 10px; letter-spacing: 0.25px;
    color: var(--ink); white-space: nowrap;
  }
  .letterhead-footer b { font-weight: 700; color: var(--ink-strong); }
  .letterhead-footer .sep { margin: 0 5px; color: var(--rule); }
  .letterhead-footer .reg { margin-top: 8px; }

  .card {
    position: absolute; left: 888px; width: 240px; height: 146px;
    box-shadow: 0 1px 3px rgba(0,0,0,.3); overflow: hidden;
  }
  .card-front { top: 430px; background: var(--charcoal); }
  .card-back { top: 606px; background: var(--yellow); }
  .card-front .shapes { position: absolute; left: 0; top: 0; }
  .card-front .brand { position: absolute; left: 94px; top: 41px; }
  .card-front .brand-name { font-size: 16px; }
  .card-details {
    position: absolute; left: 6px; top: 79px;
    color: var(--yellow); font-size: 6px; line-height: 7.6px; white-space: nowrap;
  }
  .card-details .person { font-size: 7px; font-weight: 600; letter-spacing: 0.6px; line-height: 8px; }
  .card-details .role { margin-bottom: 4px; }
  .card-details b { font-weight: 700; }
  .card-details .reg { margin-top: 4px; }
</style>
</head>
<body>

<section class="letterhead" aria-label="Letterhead">
  <svg class="stripes" width="576" height="744" viewBox="0 0 576 744" aria-hidden="true">
    <polygon points="381,0 387,0 357,82 351,89" fill="var(--yellow)"/>
    <polygon points="404,122 576,188 576,196 414,131" fill="var(--yellow)"/>
  </svg>
  <div class="brand"><span class="brand-name">Harbin Vault</span></div>
  <footer class="letterhead-footer">
    <p><b>T</b> 0498 305 217 <b>F</b> 0498 305 217<span class="sep">|</span>glen@harbinvault.com.au<span class="sep">|</span>www.harbinvault.com.au</p>
    <p>218-220 Tallowby Rd, Carrow Flats, 3094</p>
    <p class="reg"><b>ABN</b> 384 902 17736 <b>ACN</b> 293 718 406</p>
  </footer>
</section>

<section class="card card-front" aria-label="Business card front">
  <svg class="shapes" width="240" height="146" viewBox="0 0 240 146" aria-hidden="true">
    <polygon points="128,0 240,0 240,76 196,118 95,80 86,38" fill="var(--paper)"/>
    <polygon points="101,0 105,0 94,36 90,39" fill="var(--yellow)"/>
    <polygon points="95,78 196,116 193,120 100,84" fill="var(--yellow)"/>
  </svg>
  <div class="brand"><span class="brand-name">Harbin Vault</span></div>
  <div class="card-details">
    <p class="person">GLEN WHITCOMBE</p>
    <p class="role">Manager</p>
    <p><b>T</b> 0498 305 217 <b>F</b> 0498 305 217</p>
    <p>glen@harbinvault.com.au</p>
    <p>www.harbinvault.com.au</p>
    <p>218-220 Tallowby Rd, Carrow Flats, 3094</p>
    <p class="reg"><b>ABN</b> 384 902 17736 <b>ACN</b> 293 718 406</p>
  </div>
</section>

<section class="card card-back" aria-label="Business card back"></section>

</body>
</html>
```